Bright Path Flyer Design for Virtual Online Clinic. -5.5 x 8.5 inches (half sheet)

We need a clean, modern flyer design for Bright Path, a new virtual walk-in clinic based in British Columbia. The flyer will be used in libraries, pharmacies, and community centers to help residents easily access primary care through their Bright Path NFC access card.
The flyer will ask a question : NEED A DOCTOR? This should be large and attention grabbing.
The design should clearly feature a Bright Path card image (the access card) as the centerpiece and visually show how patients can use it to book appointments. The tone should feel trustworthy, healthcare-oriented, and community-friendly — clean fonts, clear spacing, and strong readability from a distance.

Side One: This card has the NFC Access Card.
NEED A DOCTOR? (Large Font, Attention Grabbing)
How to Book an Appointment using your Bright Path Card
Step 1: Tap Your Card on Your Phone
Hold your card near the back of your phone.
It will activate automatically — no app needed.
The Bright Path scheduler will open.
Step 2: Schedule Your Appointment
Select your clinical concern.
Choose your time window.
Register (only once).
Confirm your appointment.
Step 3: Relax, we’ll take care of the rest
A doctor will call during your scheduled time.
Once booked, you’ll be able to call our office.
No emails, no texts — just a real person.
It’s that simple.
Side Two:
About Bright Path
Created by Dr. Marcus Ferrigan
Bright Path was founded to make healthcare simple and convenient. Prescription renewals. Common infections. Medical notes. And so much more.
Our doctors can address 120+ health concerns virtually — providing quality care without the waiting room. No waiting rooms. Just real doctors providing real care.
Why Patients Choose Bright Path
Easy access – book and be seen from anywhere in BC.
Effortless booking – tap your Bright Path Card to begin.
Trusted physicians – every visit is with a licensed BC family doctor.
How It Works
Book your visit — choose a time window that fits your day.
Join the queue — you’ll be called when it’s your turn.
Speak directly with your doctor — simple, secure, and stress-free.
Convenient Care for Common Concerns

Additional Details.
Please find the domain to be launched soon. I've attached the NFC card file for review, it is 85.5 mm x 54 mm. The card will be glued to the flyer.
I've attached examples of flyers but they are not the look I am seeking and I am looking for creative solutions.
Thank you!
http://brightpath-example.test/

Adult Patients in British Columbia

Healthcare

• Looking for clean lines, uniform appearance, and high legibility i.e poppins

0054AA
0677BA
7BADD7
CADEEF
E8F1F8

• Need A Doctor?
• Elegant style, not too busy, clear layout.
• Clutter, look cheap - review examples.

```html
<!DOCTYPE html>
<html lang="en">
<head>
<meta charset="utf-8">
<title>Bright Path – Flyer</title>
<link rel="stylesheet" href="https://fonts.googleapis.com/css2?family=Bebas+Neue&family=Poppins:wght@300;400;500;600;700&display=swap">
<style>
  :root{
    --brand:#0b2bd4;
    --brand-band:#4a7af2;
    --accent:#3ce44f;
    --ink:#1b1d2a;
    --muted:#2e3140;
    --mist:#eef2f4;
    --line:#cfd8dc;
    --white:#ffffff;
  }
  *{box-sizing:border-box;margin:0;padding:0}
  html,body{width:1200px;height:1200px;overflow:hidden;background:var(--white)}
  body{position:relative;font-family:'Poppins',sans-serif;color:var(--ink)}
  .abs{position:absolute}
  .sheet{position:absolute;overflow:hidden;box-shadow:0 3px 6px rgba(0,0,0,.28)}

  /* ---------- Side one ---------- */
  .side-one{left:116px;top:218px;width:461px;height:713px;background:var(--brand);color:var(--white)}
  .side-one .brand{left:29px;top:38px;font-size:22px;font-weight:400;letter-spacing:.2px}
  .side-one .url{right:36px;top:47px;font-size:9.5px;font-weight:600;letter-spacing:.3px}
  .headline{left:0;width:100%;top:94px;text-align:center;font-family:'Bebas Neue',sans-serif;font-size:69px;line-height:1;letter-spacing:-.5px}
  .band{left:0;top:230px;width:100%;height:74px;background:var(--brand-band)}
  .card{left:72px;top:166px;width:315px;height:189px;background:var(--white)}
  .card .art{left:0;top:0}
  .card .card-name{left:110px;top:72px;width:175px;text-align:center;font-size:27px;font-weight:400;color:var(--brand)}
  .card .chip{left:279px;top:26px;width:13px;height:13px;background:var(--brand);border-radius:2px}
  .card .tap{left:182px;top:147px;font-size:8.8px;line-height:13px;color:var(--brand);font-weight:400;white-space:nowrap}
  .card .tap-icon{left:266px;top:145px}
  .book-title{left:0;width:100%;top:369px;text-align:center;font-size:13.6px;font-weight:500}

  .step-icon{position:absolute}
  .step-num{position:absolute;font-size:80px;font-weight:500;line-height:1}
  .checks{position:absolute;left:182px;list-style:none;font-size:9.2px;line-height:17.5px;font-weight:400}
  .checks li{position:relative;padding-left:17px;white-space:nowrap}
  .checks li.wrap{white-space:normal;width:230px;line-height:13px;padding-top:2px}
  .checks li svg{position:absolute;left:0;top:4px}
  .checks li.wrap svg{top:3px}

  /* ---------- Side two ---------- */
  .side-two{left:631px;top:218px;width:460px;height:711px;background:var(--white)}
  .about-head{left:0;top:0;width:100%;height:116px;background:var(--brand);color:var(--white)}
  .about-head .about{left:31px;top:48px;font-size:34px;font-weight:300;line-height:1}
  .about-head .brand{left:150px;top:50px;font-size:29px;font-weight:400;line-height:1}
  .about-head .creator{left:333px;top:50px;font-size:10.6px;line-height:16px;font-weight:300}
  .about-head .creator b{font-weight:600}

  .intro-brand{left:43px;top:141px;font-size:16px;font-weight:400;color:var(--brand)}
  .copy{font-size:9.2px;line-height:12.8px;color:var(--muted)}
  .intro-copy{left:41px;top:182px;width:170px}
  .stat-num{left:253px;top:142px;font-size:30px;font-weight:600;color:var(--brand);line-height:1;white-space:nowrap}
  .stat-label{left:323px;top:145px;font-size:11px;line-height:12.5px;font-weight:600;color:var(--brand)}
  .stat-copy{left:253px;top:181px;width:184px}

  .why{left:0;top:263px;width:100%;height:218px;background:var(--mist)}
  .section-title{left:0;width:100%;text-align:center;font-size:17.4px;font-weight:500;color:var(--ink)}
  .rule{height:1px;background:linear-gradient(90deg,rgba(60,228,79,0),rgba(60,228,79,.6),rgba(60,228,79,0))}
  .why .section-title{top:17px}
  .why .rule{left:162px;top:40px;width:137px}
  .why-art{left:0;top:0}
  .benefit{position:absolute;text-align:center;color:var(--ink)}
  .benefit h3{font-size:10.6px;font-weight:600;line-height:14px;margin-bottom:2px}
  .benefit p{font-size:9.4px;line-height:12.8px;color:var(--muted)}

  .how .section-title{top:495px}
  .how-rule{left:158px;top:522px;width:142px}
  .step-row{position:absolute;left:29px;width:402px;height:40px}
  .step-row .row-line{position:absolute;left:0;top:0;width:180px;height:100%;border-top:1px solid #e4e9ec;border-bottom:1px solid #e4e9ec}
  .step-row .dot{position:absolute;left:1px;top:5px;width:30px;height:30px;border-radius:50%;background:var(--brand);color:var(--white);font-size:13px;font-weight:500;display:flex;align-items:center;justify-content:center}
  .step-row .label{position:absolute;left:48px;top:0;height:100%;display:flex;align-items:center;font-size:10.6px;font-weight:600;line-height:13px}
  .step-row .detail{position:absolute;left:178px;top:0;width:224px;height:100%;background:var(--brand);border-radius:3px;color:var(--white);font-size:9.4px;display:flex;align-items:center;padding-left:12px}
  .footer-bar{left:0;bottom:0;width:100%;height:11px;background:var(--brand)}
</style>
</head>
<body>

<!-- ===== Side one: booking card ===== -->
<section class="sheet side-one">
  <div class="abs brand">Bright Path</div>
  <div class="abs url">www.brightpath-example.test</div>
  <h1 class="abs headline">NEED A DOCTOR?</h1>
  <div class="abs band"></div>

  <div class="abs card">
    <svg class="abs art" width="315" height="189" viewBox="0 0 315 189" role="img" aria-label="Card artwork: blue panel with the Bright Path bird illustration">
      <polygon points="11,11 137,11 86,178 11,178" fill="#0b2bd4"/>
    </svg>
    <div class="abs card-name">Bright Path</div>
    <div class="abs chip"></div>
    <div class="abs tap">Tap Here to Book</div>
    <svg class="abs tap-icon" width="25" height="17" viewBox="0 0 25 17" fill="none" stroke="#0b2bd4" stroke-width="1.3">
      <rect x="1" y="1.5" width="12" height="14" rx="3"/>
      <rect x="4" y="5" width="6" height="7" rx="1"/>
      <path d="M15 5.5c1.5 2 1.5 4 0 6M18 3.5c2.6 3 2.6 7 0 10M21 1.5c3.6 4.2 3.6 9.8 0 14"/>
    </svg>
  </div>

  <h2 class="abs book-title">How to book an appointment using your Bright Path card</h2>

  <!-- Step 1 -->
  <svg class="step-icon" style="left:45px;top:405px" width="66" height="68" viewBox="0 0 66 68" fill="none" stroke="#3ce44f" stroke-width="2.4" stroke-linecap="round" stroke-linejoin="round">
    <rect x="18" y="14" width="46" height="30" rx="3"/>
    <rect x="22" y="6" width="28" height="18" rx="2" fill="#0b2bd4"/>
    <line x1="22" y1="12" x2="50" y2="12"/>
    <path d="M54 4c2 1.5 2 4 0 5.5M57 1c4 3 4 9 0 12"/>
    <path d="M18 30c-5 0-9 4-10 9l-2 12M18 38h-4c-3 0-4 5-1 6h5M10 56c0 5-2 8-5 11"/>
  </svg>
  <div class="step-num" style="left:131px;top:402px">1</div>
  <ul class="checks" style="top:407px">
    <li><svg width="10" height="10" viewBox="0 0 10 10" fill="none" stroke="#3ce44f" stroke-width="1.1"><circle cx="5" cy="5" r="4.3"/><path d="M3 5.2l1.5 1.4L7.2 3.8"/></svg>Tap Your Card on Your Phone</li>
    <li><svg width="10" height="10" viewBox="0 0 10 10" fill="none" stroke="#3ce44f" stroke-width="1.1"><circle cx="5" cy="5" r="4.3"/><path d="M3 5.2l1.5 1.4L7.2 3.8"/></svg>Hold your card near the back of your phone.</li>
    <li><svg width="10" height="10" viewBox="0 0 10 10" fill="none" stroke="#3ce44f" stroke-width="1.1"><circle cx="5" cy="5" r="4.3"/><path d="M3 5.2l1.5 1.4L7.2 3.8"/></svg>It will activate automatically — no app needed.</li>
    <li><svg width="10" height="10" viewBox="0 0 10 10" fill="none" stroke="#3ce44f" stroke-width="1.1"><circle cx="5" cy="5" r="4.3"/><path d="M3 5.2l1.5 1.4L7.2 3.8"/></svg>The Bright Path scheduler will open.</li>
  </ul>

  <!-- Step 2 -->
  <svg class="step-icon" style="left:45px;top:505px" width="56" height="56" viewBox="0 0 56 56" fill="none" stroke="#3ce44f" stroke-width="2.6" stroke-linecap="round" stroke-linejoin="round">
    <rect x="5" y="14" width="48" height="39" rx="3"/>
    <line x1="5" y1="24" x2="53" y2="24"/>
    <line x1="38" y1="8" x2="38" y2="18"/><line x1="46" y1="8" x2="46" y2="18"/>
    <circle cx="16" cy="15" r="12" fill="#0b2bd4"/>
    <path d="M16 8v7l-4 4"/>
    <g stroke-width="3"><path d="M14 33h2M22 33h2M30 33h2M38 33h2M46 33h2M14 41h2M22 41h2M30 41h2M38 41h2M46 41h2"/></g>
  </svg>
  <div class="step-num" style="left:122px;top:496px">2</div>
  <ul class="checks" style="top:490px">
    <li><svg width="10" height="10" viewBox="0 0 10 10" fill="none" stroke="#3ce44f" stroke-width="1.1"><circle cx="5" cy="5" r="4.3"/><path d="M3 5.2l1.5 1.4L7.2 3.8"/></svg>Schedule Your Appointment</li>
    <li><svg width="10" height="10" viewBox="0 0 10 10" fill="none" stroke="#3ce44f" stroke-width="1.1"><circle cx="5" cy="5" r="4.3"/><path d="M3 5.2l1.5 1.4L7.2 3.8"/></svg>Select your clinical concern.</li>
    <li><svg width="10" height="10" viewBox="0 0 10 10" fill="none" stroke="#3ce44f" stroke-width="1.1"><circle cx="5" cy="5" r="4.3"/><path d="M3 5.2l1.5 1.4L7.2 3.8"/></svg>Choose your time window.</li>
    <li><svg width="10" height="10" viewBox="0 0 10 10" fill="none" stroke="#3ce44f" stroke-width="1.1"><circle cx="5" cy="5" r="4.3"/><path d="M3 5.2l1.5 1.4L7.2 3.8"/></svg>Register (only once).</li>
    <li><svg width="10" height="10" viewBox="0 0 10 10" fill="none" stroke="#3ce44f" stroke-width="1.1"><circle cx="5" cy="5" r="4.3"/><path d="M3 5.2l1.5 1.4L7.2 3.8"/></svg>Confirm your appointment.</li>
  </ul>

  <!-- Step 3 -->
  <svg class="step-icon" style="left:50px;top:598px" width="62" height="64" viewBox="0 0 62 64" fill="none" stroke="#3ce44f" stroke-width="2.4" stroke-linecap="round" stroke-linejoin="round">
    <path d="M14 8h40a4 4 0 0 1 4 4v24a4 4 0 0 1-4 4H30l-10 9v-9h-6a4 4 0 0 1-4-4V12a4 4 0 0 1 4-4z"/>
    <path d="M26 16c-2 1-2 4 0 7s6 7 9 8 5-1 5-2l-3-3-2 1c-2-1-4-3-5-5l1-2-3-4z"/>
  </svg>
  <div class="step-num" style="left:122px;top:592px">3</div>
  <ul class="checks" style="top:593px">
    <li><svg width="10" height="10" viewBox="0 0 10 10" fill="none" stroke="#3ce44f" stroke-width="1.1"><circle cx="5" cy="5" r="4.3"/><path d="M3 5.2l1.5 1.4L7.2 3.8"/></svg>Relax, we’ll take care of the rest</li>
    <li><svg width="10" height="10" viewBox="0 0 10 10" fill="none" stroke="#3ce44f" stroke-width="1.1"><circle cx="5" cy="5" r="4.3"/><path d="M3 5.2l1.5 1.4L7.2 3.8"/></svg>A doctor will call during your scheduled time.</li>
    <li><svg width="10" height="10" viewBox="0 0 10 10" fill="none" stroke="#3ce44f" stroke-width="1.1"><circle cx="5" cy="5" r="4.3"/><path d="M3 5.2l1.5 1.4L7.2 3.8"/></svg>Once booked, you’ll be able to call our office.</li>
    <li class="wrap"><svg width="10" height="10" viewBox="0 0 10 10" fill="none" stroke="#3ce44f" stroke-width="1.1"><circle cx="5" cy="5" r="4.3"/><path d="M3 5.2l1.5 1.4L7.2 3.8"/></svg>No emails, no texts — just a real person. It’s that simple.</li>
  </ul>
</section>

<!-- ===== Side two: about ===== -->
<section class="sheet side-two">
  <header class="abs about-head">
    <div class="abs about">ABOUT</div>
    <div class="abs brand">Bright Path</div>
    <div class="abs creator">Created by<br><b>Dr. Marcus Ferrigan</b></div>
  </header>

  <div class="abs intro-brand">Bright Path</div>
  <p class="abs copy intro-copy">Bright Path was founded to make healthcare simple and convenient. Prescription renewals. Common infections. Medical notes. And so much more.</p>

  <div class="abs stat-num">120+</div>
  <div class="abs stat-label">HEALTH<br>CONCERNS</div>
  <p class="abs copy stat-copy">Our doctors can address 120+ health concerns virtually — providing quality care without the waiting room. No waiting rooms. Just real doctors providing real care.</p>

  <div class="abs why">
    <h2 class="abs section-title">Why Patients Choose Bright Path</h2>
    <div class="abs rule"></div>
  </div>

  <svg class="abs why-art" width="460" height="480" viewBox="0 0 460 480" fill="#fff" stroke="#cfd8dc" stroke-width="1.5">
    <rect x="297" y="359" width="136" height="93" rx="13"/>
    <path d="M176 359H298V397l7 8-7 8V452H176Z"/>
    <path d="M47 359H165V397l7 8-7 8V452H47a13 13 0 0 1-13-13V372a13 13 0 0 1 13-13Z"/>
    <g stroke="#fff" stroke-width="1.5" fill="#0b2bd4">
      <circle cx="101" cy="350" r="26"/>
      <circle cx="237" cy="350" r="26"/>
      <circle cx="370" cy="350" r="26"/>
    </g>
    <circle cx="101" cy="350" r="27.5" fill="none" stroke="#0b2bd4" stroke-width="1"/>
    <circle cx="237" cy="350" r="27.5" fill="none" stroke="#0b2bd4" stroke-width="1"/>
    <circle cx="370" cy="350" r="27.5" fill="none" stroke="#0b2bd4" stroke-width="1"/>
    <g fill="none" stroke="#fff" stroke-width="1.6" stroke-linecap="round" stroke-linejoin="round">
      <rect x="90" y="336" width="16" height="27" rx="2.5"/>
      <rect x="98" y="342" width="14" height="10" rx="2" fill="#0b2bd4"/>
      <circle cx="95" cy="358" r="0.8"/>
      <rect x="232" y="338" width="16" height="11" rx="1.5" transform="rotate(-25 240 343)"/>
      <path d="M223 360l6-6c2-2 5-2 7 0l4 1M226 364l4-2h6"/>
      <path d="M245 336c1 1 1 3 0 4"/>
      <circle cx="370" cy="344" r="7"/>
      <path d="M358 364c0-7 5-11 12-11s12 4 12 11"/>
      <path d="M370 339v6M367 342h6"/>
    </g>
  </svg>

  <div class="benefit" style="left:38px;top:384px;width:122px">
    <h3>Easy access</h3>
    <p>Book and be seen<br>from anywhere in BC.</p>
  </div>
  <div class="benefit" style="left:172px;top:385px;width:122px">
    <h3>Effortless booking</h3>
    <p>Tap your Bright Path<br>Card to begin.</p>
  </div>
  <div class="benefit" style="left:305px;top:387px;width:126px">
    <h3>Trusted physicians</h3>
    <p>Every visit is with a licensed BC family doctor.</p>
  </div>

  <section class="how">
    <h2 class="abs section-title">How It Works</h2>
    <div class="abs rule how-rule"></div>

    <div class="step-row" style="top:538px">
      <div class="row-line"></div>
      <div class="dot">1</div>
      <div class="label">Book your visit</div>
      <div class="detail">Choose a time window that fits your day.</div>
    </div>
    <div class="step-row" style="top:590px">
      <div class="row-line"></div>
      <div class="dot">2</div>
      <div class="label">Join the queue</div>
      <div class="detail">You’ll be called when it’s your turn.</div>
    </div>
    <div class="step-row" style="top:641px">
      <div class="row-line"></div>
      <div class="dot">3</div>
      <div class="label">Speak directly with<br>your doctor</div>
      <div class="detail">Simple, secure, and stress-free.</div>
    </div>
  </section>

  <div class="abs footer-bar"></div>
</section>

</body>
</html>
```